Harbourline Electrical limited business card design

I need a business card made up it must be double sided with just my logo and some graphic one side and then on the reverse a little description of services I provide along with my email address phone number and face book and instagram handles
I already had a logo designed by pixel meadow and the social media pack so I’m thinking to use the social media design as the main image
Services I provide are: domestic commercial industrial sub contract from bathroom's and kitchen’s to outside lights and sockets no job to big or to small

Industry/Entity Type

Electrician/construction industry

Contact Information for Business Card

Email address: harbourlineelectrical@mailvane.com mobile number: 07855402917 fb: Harbourline Electrical insta: @harbourlineelectrical

Font styles to use
Sans Serif

Colors
0094D4
00A9DD
6FCCEA
C7EBF8
E9F6FB
FFF300
FFF600
FEFA6F
FFFEC7
FFFEE8

Requirements
Must have
• Double sided, fb and insta handles contact info, domestic commercial industrial sub contract
Nice to have
• From bathroom's and kitchen’s to outside outside lights and sockets no job to big or to small

```html
<!DOCTYPE html>
<html lang="en">
<head>
<meta charset="utf-8">
<title>Harbourline Electrical – Business Cards</title>
<link href="https://fonts.googleapis.com/css2?family=Montserrat:wght@500;600;800&display=swap" rel="stylesheet">
<style>
  :root {
    --board: #d9dadc;
    --card: #f9f9f9;
    --blue: #0a8ac6;
    --blue-soft: #6fccea;
    --blue-tint: #c7ebf8;
    --orange: #e9ab2e;
    --orange-light: #f7c74a;
    --ink: #1c1c1c;
    --white: #ffffff;
  }
  * { margin: 0; padding: 0; box-sizing: border-box; }
  html, body { width: 1200px; height: 1200px; overflow: hidden; }
  body { background: var(--board); font-family: "Montserrat", Arial, sans-serif; position: relative; }

  .card { position: absolute; background: var(--card); overflow: hidden; }
  .card--front-landscape { left: 73px; top: 179px; width: 513px; height: 297px;
    background: radial-gradient(ellipse at 40% 50%, #ffffff 0%, #ececec 100%); }
  .card--back-landscape  { left: 615px; top: 179px; width: 514px; height: 297px; }
  .card--front-portrait  { left: 289px; top: 505px; width: 297px; height: 514px; }
  .card--back-portrait   { left: 615px; top: 505px; width: 297px; height: 514px; }

  .art { position: absolute; }

  .wordmark { position: absolute; color: var(--blue); font-weight: 800; line-height: 1; text-align: center; }
  .wordmark span { display: block; }
  .wordmark .wordmark__sub { letter-spacing: 0.55em; margin-top: 0.35em; }
  .emblem { position: absolute; border-radius: 50%; background: var(--blue-tint); }

  .contact { position: absolute; font-size: 12px; font-weight: 500; color: var(--ink); }
  .contact__row { display: flex; align-items: center; gap: 5px; height: 15px; white-space: nowrap; }
  .contact__gap { height: 14px; }
  .icon { width: 10px; height: 10px; flex: none; }
  .dot { width: 8px; height: 8px; border-radius: 50%; background: var(--orange); flex: none; margin: 0 1px; }

  .services { position: absolute; font-size: 10.5px; font-weight: 600; line-height: 13.3px;
    text-transform: uppercase; letter-spacing: 0.02em; }
  .card--back-landscape .services { color: var(--blue); }

  .divider { position: absolute; left: 208px; top: 38px; width: 2px; height: 221px; background: var(--blue); }

  .band { position: absolute; left: 0; bottom: 0; width: 100%; height: 130px; background: var(--blue); }
  .band .services { color: var(--white); left: 47px; top: 36px; width: 225px; }
</style>
</head>
<body>

<!-- Front, landscape -->
<section class="card card--front-landscape">
  <svg class="art" width="513" height="297" viewBox="0 0 513 297">
    <path role="img" aria-label="Greek key ornament arc" d="M0 0 H8 Q20 140 115 205 L95 230 Q0 160 0 0 Z" fill="var(--blue-soft)"/>
    <path role="img" aria-label="Large lightning bolt graphic" d="M285 0 H360 L12 297 Z" fill="url(#boltFade)"/>
    <polygon points="513,235 513,297 440,297" fill="var(--orange)"/>
    <defs>
      <linearGradient id="boltFade" x1="1" y1="0" x2="0" y2="1">
        <stop offset="0" stop-color="var(--orange-light)"/>
        <stop offset="1" stop-color="var(--orange)"/>
      </linearGradient>
    </defs>
  </svg>
  <div class="emblem" style="left:352px; top:92px; width:82px; height:82px;"></div>
  <div class="wordmark" style="left:300px; top:190px; width:186px; font-size:22px;">
    <span>HARBOURLINE</span><span class="wordmark__sub" style="font-size:9px;">ELECTRICAL</span>
  </div>
</section>

<!-- Back, landscape -->
<section class="card card--back-landscape">
  <div class="emblem" style="left:80px; top:104px; width:60px; height:60px;"></div>
  <div class="wordmark" style="left:30px; top:186px; width:146px; font-size:17px;">
    <span>HARBOURLINE</span><span class="wordmark__sub" style="font-size:7.5px;">ELECTRICAL</span>
  </div>
  <div class="divider"></div>
  <div class="contact" style="left:241px; top:62px;">
    <div class="contact__row">
      <svg class="icon" viewBox="0 0 10 10"><rect x="0" y="2" width="10" height="7" fill="var(--orange)"/><path d="M0 2 L5 6 L10 2" stroke="#fff" stroke-width="1" fill="none"/></svg>
      harbourlineelectrical@mailvane.com
    </div>
    <div class="contact__row">
      <svg class="icon" viewBox="0 0 10 10"><rect x="2" y="0" width="6" height="10" rx="1.2" fill="var(--orange)"/><rect x="3" y="1.3" width="4" height="6" fill="#fff"/><circle cx="5" cy="8.7" r="0.6" fill="#fff"/></svg>
      078 5540 2917
    </div>
    <div class="contact__gap"></div>
    <div class="contact__row"><span class="dot"></span>harbourline electrical</div>
    <div class="contact__row"><span class="dot"></span>@harbourlineelectrical</div>
  </div>
  <p class="services" style="left:241px; top:177px; width:232px;">
    Domestic commercial industrial sub contract from bathroom's and kitchen's to outside lights and sockets no job to big or to small
  </p>
</section>

<!-- Front, portrait -->
<section class="card card--front-portrait">
  <svg class="art" width="297" height="514" viewBox="0 0 297 514">
    <circle role="img" aria-label="Raised fist emblem inside a Greek key circle" cx="297" cy="262" r="258" fill="var(--blue)"/>
    <circle cx="297" cy="262" r="222" fill="var(--blue-soft)"/>
    <path role="img" aria-label="Lightning bolt graphic" d="M8 0 H58 L205 170 L140 200 Z" fill="var(--orange-light)"/>
  </svg>
  <div class="wordmark" style="left:26px; top:476px; width:132px; font-size:17px; text-align:left;">
    <span>HARBOURLINE</span><span class="wordmark__sub" style="font-size:7px;">ELECTRICAL</span>
  </div>
</section>

<!-- Back, portrait -->
<section class="card card--back-portrait">
  <div class="emblem" style="left:103px; top:60px; width:90px; height:90px;"></div>
  <div class="wordmark" style="left:40px; top:170px; width:217px; font-size:25px;">
    <span>HARBOURLINE</span><span class="wordmark__sub" style="font-size:11px;">ELECTRICAL</span>
  </div>
  <div class="contact" style="left:47px; top:291px;">
    <div class="contact__row">
      <svg class="icon" viewBox="0 0 10 10"><rect x="0" y="2" width="10" height="7" fill="var(--orange)"/><path d="M0 2 L5 6 L10 2" stroke="#fff" stroke-width="1" fill="none"/></svg>
      harbourlineelectrical@mailvane.com
    </div>
    <div class="contact__row">
      <svg class="icon" viewBox="0 0 10 10"><rect x="2" y="0" width="6" height="10" rx="1.2" fill="var(--orange)"/><rect x="3" y="1.3" width="4" height="6" fill="#fff"/><circle cx="5" cy="8.7" r="0.6" fill="#fff"/></svg>
      078 5540 2917
    </div>
    <div class="contact__gap"></div>
    <div class="contact__row"><span class="dot"></span>harbourline electrical</div>
    <div class="contact__row"><span class="dot"></span>@harbourlineelectrical</div>
  </div>
  <div class="band">
    <p class="services">
      Domestic commercial industrial sub contract from bathroom's and kitchen's to outside lights and sockets no job to big or to small
    </p>
  </div>
</section>

</body>
</html>
```